HR services to some of biggest Silicon Valley Tech companies needs a new website

We need a new website design probably 4-5 pages initially. Here are some websites we like the look of https://quillmarkgroup.example/ , https://www.vantrel.example/ and https://pemvio.example/ .

Target Market(s)

Silicon valley tech companies

Industry/Entity Type

HR

Coding

Coded - Design and coding required

Number of Pages Required

5+ page

Requirements
Nice to have
• any stock photos or images should show a diverse group of people. Our client base is very diverse

```html
<!DOCTYPE html>
<html lang="en">
<head>
<meta charset="utf-8">
<title>Quorvane HR Consulting</title>
<link href="https://fonts.googleapis.com/css2?family=Roboto:wght@400;500;700;900&display=swap" rel="stylesheet">
<style>
:root{
  --yellow:#ffc20e;
  --yellow-soft:#ffd34d;
  --ice:#eaf3fc;
  --ink:#1c1c1c;
  --text:#3a3a3a;
  --muted:#6b6b6b;
  --footer:#1e1e1e;
  --white:#ffffff;
}
*{box-sizing:border-box;margin:0;padding:0}
html,body{width:1200px;height:4655px;overflow:hidden}
body{font-family:'Roboto',Arial,sans-serif;color:var(--text);background:var(--white);position:relative}
.abs{position:absolute}
.btn{position:absolute;display:flex;align-items:center;justify-content:center;border-radius:22px;font-weight:700;font-size:14px;color:var(--ink);text-transform:uppercase;letter-spacing:.3px}
.btn-fill{background:var(--yellow)}
.btn-line{border:2px solid var(--ink)}
h2.title{font-weight:700;color:var(--ink);text-transform:uppercase;line-height:1.1}

/* header */
.header{top:0;left:0;width:1200px;height:85px;background:var(--white)}
.brand{left:99px;top:30px;display:flex;align-items:center;gap:8px;font-weight:700;font-size:17px;color:var(--ink)}
.brand i{width:14px;height:14px;background:var(--yellow);border-radius:50%;display:block}
.nav{top:32px;font-size:15px;color:var(--ink);font-weight:500}
.phone{left:802px;top:30px;display:flex;align-items:center;gap:8px;font-weight:700;font-size:16px;color:var(--ink)}
.nav-sep{left:777px;top:28px;width:1px;height:28px;background:#ddd}

/* hero */
.hero{top:85px;left:0;width:1200px;height:611px;background:linear-gradient(100deg,#4a4f56 0%,#7d8791 40%,#c2c9cf 60%,#5e6b77 100%)}
.hero-title{left:99px;top:258px;font-size:62px;font-weight:900;color:var(--white);line-height:1;text-transform:uppercase}
.hero-sub{left:99px;top:392px;font-size:31px;color:var(--white);font-weight:500}
.arrow{width:22px;height:40px}
.dots{display:flex;gap:12px}
.dots span{width:11px;height:11px;border-radius:50%;background:#c9c9c9}
.dots span.on{background:var(--white);box-shadow:0 0 0 2px rgba(255,255,255,.5)}

/* solution */
.sol-photo{left:112px;top:790px;width:470px;height:511px;border-radius:6px;background:linear-gradient(135deg,#c9d3db,#8a97a3 55%,#5b6b7c)}
.sol-title{left:634px;top:848px;font-size:38px;width:480px}
.ticks{list-style:none}
.ticks li{position:relative;padding-left:24px;font-size:14px;line-height:24px;margin-bottom:18px}
.ticks li::before{content:"»";position:absolute;left:0;top:-4px;font-size:22px;color:var(--yellow);font-weight:700}

/* years */
.years{left:22px;top:1395px;width:1156px;height:752px;background:var(--ice);border-radius:24px}
.years-title{left:108px;top:1484px;font-size:37px}
.years-text{left:108px;top:1590px;width:430px;font-size:14px;line-height:27px}
.years-text p{margin-bottom:18px}
.card{position:absolute;left:609px;width:482px;height:124px;background:var(--white);border-radius:8px}
.card .ic{position:absolute;left:14px;top:30px}
.card p{position:absolute;left:80px;top:24px;width:318px;font-size:12.5px;line-height:22px}
.card b{position:absolute;right:14px;top:26px;font-size:60px;font-weight:900;color:#e6eff9}

/* team */
.team{left:99px;top:1995px;width:1001px;height:528px;background:var(--yellow);border-radius:22px;overflow:hidden}
.team-photo{left:190px;top:1943px;width:406px;height:580px;background:linear-gradient(180deg,#e6c9a8 0%,#c49874 25%,#2d3b52 45%,#1e2a3d 100%);border-radius:200px 200px 0 0}
.team-title{left:634px;top:2064px;font-size:38px}
.team-list li{font-size:16.5px;line-height:24px;margin-bottom:16px;padding-left:32px}
.team-list li::before{color:var(--ink);font-size:24px}

/* services */
.svc-title{left:0;top:2608px;width:1200px;text-align:center;font-size:37px}
.svc-sub{left:0;top:2664px;width:1200px;text-align:center;font-size:15px;font-weight:700;color:var(--ink);line-height:27px}
.svc{position:absolute;width:436px;height:294px;background:var(--white);border-radius:8px;box-shadow:0 2px 14px rgba(0,0,0,.08)}
.svc .badge{position:absolute;left:20px;top:22px;width:78px;height:78px;border-radius:50%;background:var(--yellow);display:flex;align-items:center;justify-content:center}
.svc h3{position:absolute;left:114px;top:50px;font-size:18px;font-weight:500;color:var(--ink)}
.svc ul{position:absolute;left:36px;top:122px;width:380px}
.svc ul li{font-size:13px;line-height:20px;margin-bottom:5px;padding-left:20px}
.svc ul li::before{font-size:17px;top:-2px}

/* testimonials */
.testi-bg{left:0;top:3460px;width:1200px;height:533px;background:var(--ice)}
.testi-title{left:0;top:3536px;width:1200px;text-align:center;font-size:37px}
.tcard{position:absolute;top:3614px;width:318px;height:244px;background:var(--white);border-radius:6px}
.tcard h4{position:absolute;left:16px;top:28px;font-size:17px;font-weight:700;color:var(--ink)}
.tcard p{position:absolute;left:16px;top:62px;width:288px;font-size:12px;line-height:23px;color:var(--muted)}
.tcard .who{position:absolute;left:16px;top:186px;display:flex;align-items:center;gap:10px;font-size:14px;color:var(--ink);font-weight:500}
.tcard .who i{width:34px;height:34px;border-radius:50%;background:#b7c0c8;display:block}
.tcard .q{position:absolute;right:18px;top:178px;font-size:70px;line-height:1;color:#d8d8d8;font-family:Georgia,serif}

/* newsletter */
.news{left:0;top:3993px;width:1200px;height:326px;background:linear-gradient(180deg,#f1b80b,#ffc926)}
.news-title{left:0;top:4088px;width:1200px;text-align:center;font-size:37px;color:var(--white)}
.news-sub{left:0;top:4144px;width:1200px;text-align:center;font-size:14px;color:var(--white)}
.field{position:absolute;top:4181px;height:42px;border-radius:21px;background:var(--white);font-size:12px;color:var(--ink);padding:15px 18px}
.signup{left:819px;top:4181px;width:135px;height:42px;background:#333;color:var(--white);font-size:13px}

/* footer */
.footer{left:0;top:4319px;width:1200px;height:336px;background:var(--footer)}
.f-brand{left:99px;top:4430px;display:flex;align-items:center;gap:12px;font-size:30px;font-weight:700;color:var(--white)}
.f-brand i{width:26px;height:26px;background:var(--yellow);display:block}
.f-col h5{font-size:14px;font-weight:700;color:var(--white);margin-bottom:14px}
.f-col li{list-style:none;font-size:12.5px;color:var(--white);line-height:27px}
.contact-row{display:flex;align-items:center;gap:10px;font-size:12.5px;color:var(--white);margin-bottom:14px;line-height:16px}
.contact-row span.c{width:30px;height:30px;border-radius:50%;background:var(--white);display:flex;align-items:center;justify-content:center;flex:none}
.f-rule{left:99px;top:4580px;width:1001px;height:1px;background:#555}
.copy{left:99px;top:4610px;font-size:12px;color:var(--white)}
.social{left:925px;top:4600px;display:flex;gap:10px}
.social span{width:36px;height:36px;border-radius:50%;background:var(--white);display:block}
</style>
</head>
<body>

<!-- header -->
<div class="abs header"></div>
<div class="abs brand"><i></i>Quorvane HR</div>
<div class="abs nav" style="left:388px">ABOUT US</div>
<div class="abs nav" style="left:497px">SERVICES</div>
<div class="abs nav" style="left:600px">BLOG</div>
<div class="abs nav" style="left:674px">CONTACT</div>
<div class="abs nav-sep"></div>
<div class="abs phone">
  <svg width="16" height="16" viewBox="0 0 24 24"><path d="M6.6 10.8a15 15 0 006.6 6.6l2.2-2.2a1 1 0 011-.25 11.4 11.4 0 003.6.57 1 1 0 011 1V20a1 1 0 01-1 1A17 17 0 013 4a1 1 0 011-1h3.5a1 1 0 011 1c0 1.25.2 2.45.57 3.57a1 1 0 01-.25 1z" fill="#ffc20e"/></svg>
  555-010-2468
</div>
<div class="btn btn-line" style="left:961px;top:22px;width:138px;height:39px;border-color:var(--yellow)">Contact</div>

<!-- hero -->
<div class="abs hero" role="img" aria-label="Photo of a consultant taking notes in a meeting with a client"></div>
<div class="abs hero-title">Quorvane HR<br>Consulting</div>
<div class="abs hero-sub">Our Team Supports Yours</div>
<div class="btn btn-fill" style="left:99px;top:457px;width:174px;height:38px">Get Started</div>
<svg class="abs arrow" style="left:62px;top:370px" viewBox="0 0 22 40"><path d="M20 2L3 20l17 18" fill="none" stroke="#fff" stroke-width="2"/></svg>
<svg class="abs arrow" style="left:1112px;top:370px" viewBox="0 0 22 40"><path d="M2 2l17 18L2 38" fill="none" stroke="#fff" stroke-width="2"/></svg>
<div class="abs dots" style="left:558px;top:662px"><span></span><span class="on"></span><span></span><span></span></div>

<!-- solution -->
<svg class="abs" style="left:940px;top:696px" width="260" height="250" viewBox="0 0 260 250"><circle cx="250" cy="130" r="200" fill="none" stroke="#fff3cc" stroke-width="22"/></svg>
<div class="abs sol-photo" role="img" aria-label="Photo of two colleagues shaking hands in an office"></div>
<h2 class="abs title sol-title">Your Human Resources Solution</h2>
<ul class="abs ticks" style="left:634px;top:957px;width:470px">
  <li>Quorvane HR Consulting is the solution to all your HR issues. We are a one-stop-shop providing a variety of services</li>
  <li>Whether you have a specific HR need or seek relief by outsourcing altogether, we have you covered</li>
  <li>For some clients, a Quorvane HR Consultant is known as the HR department and for others, we simply step in as needed on a project basis</li>
</ul>
<div class="btn btn-fill" style="left:634px;top:1196px;width:199px;height:42px">Let's Collaborate!</div>

<!-- years -->
<div class="abs years"></div>
<h2 class="abs title years-title">Celebrating 15 Years<br>in Business</h2>
<div class="abs years-text">
  <p>Lorem ipsum dolor sit amet, consectetur adipiscing elit, sed do eiusmod tempor incididunt ut lore et dolore magna aliqua. Quis ipsum suspendisse ultrices gravida. Risusodo viverra maecenas accumsan lacus vel facilisis.</p>
  <p>Lorem ipsum dolor sit amet, consectetur adipiscing elit, sed do eiusmod tempor incididunt ut lore et dolore magna aliqua. Quis ipsum suspendisse ultrices gravida</p>
</div>
<div class="btn btn-fill" style="left:108px;top:1814px;width:201px;height:42px">Get Started</div>

<div class="card" style="top:1487px">
  <svg class="ic" width="58" height="60" viewBox="0 0 58 60" fill="none" stroke="#222" stroke-width="2"><circle cx="29" cy="14" r="9"/><path d="M12 52c0-12 8-20 17-20s17 8 17 20z"/><path d="M29 32v12"/></svg>
  <p>For fifteen years our team of industry experts has been providing HR consulting services with innovative strategies and a partnership mentality</p><b>01</b>
</div>
<div class="card" style="top:1625px">
  <svg class="ic" width="58" height="60" viewBox="0 0 58 60" fill="none" stroke="#222" stroke-width="2"><circle cx="20" cy="22" r="10"/><circle cx="20" cy="22" r="4"/><circle cx="42" cy="38" r="8"/><circle cx="42" cy="38" r="3"/><circle cx="22" cy="48" r="5"/></svg>
  <p>We have worked with some of the most innovative companies in Silicon Valley, across a broad range of industries, and we're proud to grow our client list every year</p><b>02</b>
</div>
<div class="card" style="top:1762px">
  <svg class="ic" width="58" height="60" viewBox="0 0 58 60" fill="none" stroke="#222" stroke-width="2"><rect x="18" y="6" width="22" height="16" rx="2"/><path d="M8 54l12-18h18l12 18M20 36l9-10 9 10"/></svg>
  <p>Quorvane's experienced professionals help implement and maintain best practices, allowing our clients to focus on their core competencies</p><b>03</b>
</div>

<!-- team -->
<div class="abs team">
  <svg class="abs" style="left:600px;top:250px" width="420" height="300"><circle cx="300" cy="230" r="200" fill="#ffd24a"/></svg>
  <svg class="abs" style="left:0;top:0" width="420" height="300"><circle cx="230" cy="80" r="160" fill="#ffcb2e"/></svg>
</div>
<div class="abs team-photo" role="img" aria-label="Portrait of the company's CEO in a dark blazer, arms crossed"></div>
<h2 class="abs title team-title">Our Team</h2>
<ul class="abs ticks team-list" style="left:634px;top:2128px;width:430px">
  <li>Our team is woman-owned, women-led &amp; partnership</li>
  <li>Working with us means you're hiring senior-level talent that acts as an extension of your company</li>
  <li>We're here to educate companies and help them solve complex HR problems</li>
  <li>Information about our CEO, Renata Okafor, can be found here</li>
</ul>
<div class="btn btn-line" style="left:636px;top:2405px;width:199px;height:42px">Meet Our Team</div>

<!-- services -->
<svg class="abs" style="left:0;top:3050px" width="200" height="410"><circle cx="10" cy="300" r="180" fill="none" stroke="#fff5d6" stroke-width="20"/></svg>
<h2 class="abs title svc-title">Our Services</h2>
<p class="abs svc-sub">We help assess your HR needs and offer ongoing HR Department services or defined projects based<br>on your organization's unique needs and goals</p>

<div class="svc" style="left:150px;top:2756px">
  <div class="badge"><svg width="40" height="40" viewBox="0 0 40 40" fill="none" stroke="#222" stroke-width="2"><circle cx="20" cy="20" r="13"/><path d="M13 20l5 5 9-10"/></svg></div>
  <h3>Setup</h3>
  <ul class="ticks">
    <li>Select and implement an HRIS system</li>
    <li>Create Company Handbook</li>
    <li>Write termination procedure</li>
    <li>Set up benefits services</li>
    <li>Set up workers comp vendor</li>
    <li>Create job descriptions for current and anticipated roles</li>
  </ul>
</div>
<div class="svc" style="left:614px;top:2756px">
  <div class="badge"><svg width="40" height="40" viewBox="0 0 40 40" fill="none" stroke="#222" stroke-width="2"><circle cx="10" cy="12" r="4"/><circle cx="20" cy="9" r="4"/><circle cx="30" cy="12" r="4"/><path d="M6 32v-8h28v8M20 14v10"/></svg></div>
  <h3>Managing HR Functions/Recruiting</h3>
  <ul class="ticks">
    <li>Onboarding/Offboarding</li>
    <li>Employee relations</li>
    <li>Investigations</li>
    <li>Leave administration</li>
    <li>Immigration liaison</li>
    <li>Compensation management</li>
  </ul>
</div>
<div class="svc" style="left:150px;top:3074px">
  <div class="badge"><svg width="40" height="40" viewBox="0 0 40 40" fill="none" stroke="#222" stroke-width="2"><rect x="8" y="6" width="24" height="18" rx="2"/><circle cx="12" cy="32" r="3"/><circle cx="20" cy="32" r="3"/><circle cx="28" cy="32" r="3"/></svg></div>
  <h3>Recurring Procedures</h3>
  <ul class="ticks">
    <li>Review handbook annually</li>
    <li>Roll out training (required and soft skills training)</li>
    <li>Write offer letters</li>
    <li>Handle employee data and files</li>
    <li>Conduct I-9 audits</li>
    <li>Handle merit and review bonuses</li>
  </ul>
</div>
<div class="svc" style="left:614px;top:3074px">
  <div class="badge"><svg width="40" height="40" viewBox="0 0 40 40" fill="none" stroke="#222" stroke-width="2"><path d="M4 20l8-8 8 6 8-6 8 8-12 10z"/><path d="M14 22l6 5"/></svg></div>
  <h3>Partner Communications &amp; Projects</h3>
  <ul class="ticks">
    <li>Manage annual bidding process for benefits review</li>
    <li>Handle workers compensation claims administration</li>
    <li>Manage leave administration between client, employee and vendor(s)</li>
    <li>Handle EDD inquires</li>
    <li>Partner on M&amp;A activity</li>
  </ul>
</div>

<!-- testimonials -->
<div class="abs testi-bg"></div>
<h2 class="abs title testi-title">Testimonials</h2>
<svg class="abs arrow" style="left:62px;top:3708px" viewBox="0 0 22 40"><path d="M20 2L3 20l17 18" fill="none" stroke="#333" stroke-width="2"/></svg>
<svg class="abs arrow" style="left:1112px;top:3708px" viewBox="0 0 22 40"><path d="M2 2l17 18L2 38" fill="none" stroke="#333" stroke-width="2"/></svg>
<div class="tcard" style="left:101px"><h4>FINIBUS BONORUM ET MALOR</h4><p>Sed ut perspiciatis unde omnis iste natus error sit voluptatem accusantium doloremque laudantium, totam rem aperiam, eaque ipsa qu ab illo inventore veritatis et quasi architecto beatae vitae dicta sunt explicabo. Nemo enim ipsam</p><div class="who"><i role="img" aria-label="Client portrait"></i>Dana Whitfield</div><span class="q">&#8220;</span></div>
<div class="tcard" style="left:441px"><h4>FINIBUS BONORUM ET MALOR</h4><p>Sed ut perspiciatis unde omnis iste natus error sit voluptatem accusantium doloremque laudantium, totam rem aperiam, eaque ipsa qu ab illo inventore veritatis et quasi architecto beatae vitae dicta sunt explicabo. Nemo enim ipsam</p><div class="who"><i role="img" aria-label="Client portrait"></i>Dana Whitfield</div><span class="q">&#8220;</span></div>
<div class="tcard" style="left:782px"><h4>FINIBUS BONORUM ET MALOR</h4><p>Sed ut perspiciatis unde omnis iste natus error sit voluptatem accusantium doloremque laudantium, totam rem aperiam, eaque ipsa qu ab illo inventore veritatis et quasi architecto beatae vitae dicta sunt explicabo. Nemo enim ipsam</p><div class="who"><i role="img" aria-label="Client portrait"></i>Dana Whitfield</div><span class="q">&#8220;</span></div>
<div class="abs dots" style="left:558px;top:3898px"><span></span><span></span><span class="on" style="background:#222;box-shadow:none"></span><span></span></div>

<!-- newsletter -->
<div class="abs news"></div>
<h2 class="abs title news-title">Subscribe Our Newsletter</h2>
<p class="abs news-sub">Sed ut perspiciatis unde omnis iste natus error sit voluptatem</p>
<div class="field" style="left:271px;width:260px">Your name</div>
<div class="field" style="left:546px;width:260px">Email address</div>
<div class="btn signup">Sign Up</div>

<!-- footer -->
<div class="abs footer"></div>
<div class="abs f-brand"><i></i>Quorvane HR</div>
<div class="abs f-col" style="left:457px;top:4388px"><h5>QUICK LINKS</h5><ul><li>Home</li><li>About Us</li><li>Services</li><li>Blog</li><li>Contact</li></ul></div>
<div class="abs f-col" style="left:669px;top:4388px"><h5>MORE</h5><ul><li>Privacy policy</li><li>Terms and conditio</li><li>Sitemap</li><li>Help</li></ul></div>
<div class="abs f-col" style="left:893px;top:4388px;width:220px">
  <h5>CONTACT INFO</h5>
  <div class="contact-row"><span class="c"><svg width="14" height="14" viewBox="0 0 24 24"><path d="M12 2a7 7 0 00-7 7c0 5 7 13 7 13s7-8 7-13a7 7 0 00-7-7zm0 9.5A2.5 2.5 0 1112 6.5a2.5 2.5 0 010 5z" fill="#222"/></svg></span>123 Your Adress Goes Here.<br>US, 1234567</div>
  <div class="contact-row"><span class="c"><svg width="14" height="14" viewBox="0 0 24 24"><path d="M6.6 10.8a15 15 0 006.6 6.6l2.2-2.2a1 1 0 011-.25 11.4 11.4 0 003.6.57 1 1 0 011 1V20a1 1 0 01-1 1A17 17 0 013 4a1 1 0 011-1h3.5a1 1 0 011 1c0 1.25.2 2.45.57 3.57a1 1 0 01-.25 1z" fill="#222"/></svg></span>+555-010-2468</div>
  <div class="contact-row"><span class="c"><svg width="14" height="14" viewBox="0 0 24 24"><path d="M3 5h18v14H3z M3 5l9 8 9-8" fill="none" stroke="#222" stroke-width="2"/></svg></span>info@quorvanehr.example</div>
</div>
<div class="abs f-rule"></div>
<div class="abs copy">Copyright © 2021 Quorvane HR Consulting. All rights reserved.</div>
<div class="abs social"><span></span><span></span><span></span><span></span></div>

</body>
</html>
```